Amber Threshold

We need a book cover design for a new company based in Atlanta called Brightwell Counseling. I am a psychologist. My company does seminars and provides counseling to couples struggling in their marriage and questioning whether to continue. We would like to see designs that communicates peace love and happiness,

Please make sure the the design is ready for print including front, back, and spine. File needs to be an editable layered PSD file. Back cover should include space to add the isbn,bar code, bio picture, and testimonials. Use high quality stock photo. The size is 6″ x 9″ . Name should be listed as Dr. Denise Okafor PhD

Reason: The back cover and spine needs to be included

```html
<!DOCTYPE html>
<html lang="en">
<head>
<meta charset="utf-8">
<title>Amber Threshold — Book Cover</title>
<link rel="stylesheet" href="https://fonts.googleapis.com/css2?family=Quicksand:wght@500;600&family=Arimo&display=swap">
<style>
  :root {
    --brown: #8b5226;
    --orange: #d46d22;
    --peach: #f7cba0;
    --cream: #f9e8d6;
    --white: #ffffff;
    --page: #ffffff;
  }
  * { margin: 0; padding: 0; box-sizing: border-box; }
  html, body { width: 1200px; height: 836px; overflow: hidden; background: var(--page); }
  .cover { position: relative; width: 1200px; height: 836px; overflow: hidden; }

  .back-panel { position: absolute; left: 0; top: 0; width: 636px; height: 836px; background: var(--brown); }
  .bio-photo-slot { position: absolute; left: 76px; top: 57px; width: 127px; height: 167px; background: var(--white); }
  .isbn-slot { position: absolute; left: 331px; top: 687px; width: 172px; height: 97px; background: var(--white); }
  .back-copy {
    position: absolute; left: 72px; top: 258px; width: 433px;
    font-family: "Arimo", Arial, sans-serif; font-size: 13.4px; line-height: 19.6px;
    letter-spacing: 0.9px; color: var(--white); text-align: justify;
  }
  .back-title { position: absolute; left: 80px; top: 690px; font-family: "Quicksand", sans-serif; font-weight: 500; color: var(--peach); line-height: 1; }
  .back-title .line-one { display: block; font-size: 46px; letter-spacing: 1px; }
  .back-title .line-two { display: block; font-size: 30px; letter-spacing: 5px; margin-top: 8px; }

  .spine { position: absolute; left: 560px; top: 0; width: 76px; height: 836px; }
  .spine-title, .spine-author {
    position: absolute; writing-mode: vertical-rl; font-family: "Quicksand", sans-serif;
    font-weight: 500; color: var(--cream); white-space: nowrap; line-height: 1;
  }
  .spine-title { left: 14px; top: 90px; font-size: 34px; letter-spacing: 1px; }
  .spine-author { left: 22px; top: 470px; font-size: 24px; letter-spacing: 3px; }

  .front-panel { position: absolute; left: 636px; top: 0; width: 564px; height: 836px; background: var(--white); }
  .front-photo {
    position: absolute; left: 0; top: 0; width: 564px; height: 836px;
    background:
      linear-gradient(180deg, #ffffff 0%, #ffffff 24%, rgba(255,255,255,0) 42%),
      linear-gradient(90deg, #d9cbb8 0%, #f3ecdc 40%, #e6b57a 72%, #e9a640 100%);
  }
  .front-title { position: absolute; left: 100px; top: 36px; font-family: "Quicksand", sans-serif; font-weight: 500; line-height: 1; }
  .front-title .line-one { display: block; font-size: 82px; color: var(--brown); letter-spacing: 2px; }
  .front-title .line-two { display: block; font-size: 58px; color: var(--orange); letter-spacing: 5px; margin-top: 10px; }
  .front-author {
    position: absolute; left: 102px; top: 202px; font-family: "Quicksand", sans-serif;
    font-weight: 600; font-size: 21px; letter-spacing: 4px; color: var(--orange);
  }
</style>
</head>
<body>
<main class="cover">
  <section class="back-panel">
    <div class="bio-photo-slot"></div>
    <p class="back-copy">
      educational institution offering entry level and advanced programs for the animation, film and game industries
      has received confirmation that they have been nominated in Forward Steps
      Awards presented by Small Business Northvale and the Harborline Insurance Council
      has been nominated for awards in the Best Concept and Best Community Impact.
      The Best Concept award recognizes companies that have been in business in British Columbia for less than 24 months with less than 50 employees.
      The winner demonstrates a strong business concept and be able to pitch their concept to a panel of judges.
      Meanwhile, the Best Community Impact award honors companies that have demonstrated a positive impact in the community and have also made a positive impact by investing in the community.
    </p>
    <h2 class="back-title"><span class="line-one">AMBER</span><span class="line-two">THRESHOLD</span></h2>
    <div class="isbn-slot"></div>
  </section>

  <section class="spine">
    <span class="spine-title">AMBER THRESHOLD</span>
    <span class="spine-author">Dr. DENISE OKAFOR</span>
  </section>

  <section class="front-panel">
    <div class="front-photo" role="img" aria-label="Stock photo of a smiling couple resting foreheads together, the woman in a yellow top holding red tulips"></div>
    <h1 class="front-title"><span class="line-one">AMBER</span><span class="line-two">THRESHOLD</span></h1>
    <p class="front-author">Dr. DENISE OKAFOR</p>
  </section>
</main>
</body>
</html>
```